Funky Business card design for starting out career counsellor - Melbourne, Australia

Hi there, I am seeking a business card design to send straight to print. I work from a psycho-spiritual framework (existential, non-dual, transpersonal) framework and was hoping for something that is modern, funky - yet has an established grounded feel to it, but pushes the edge of art and boundary. Minimal design is good.
I don't have a corporate identity other than my wordpress template at www.pathwaybrightly.com. I like the depth of the this wordpress template, with the thought provaking image. A design that aligns to the wordpress template would be awesome (but unique is okay too).
Thanks for your help :)
Contact details for card:
Marcus Halbrenn Registered Career Counsellor marcus@pathwaybrightly.com
(existential, non-dual, transpersonal)
www.pathwaybrightly.com +61 (0) 412 968 204 Melbourne CBD & Globally on VoxLink

```html
<!DOCTYPE html>
<html lang="en">
<head>
<meta charset="utf-8">
<title>Pathway Brightly – Business Card</title>
<link rel="stylesheet" href="https://fonts.googleapis.com/css2?family=Open+Sans:wght@400;600;700&display=swap">
<style>
  :root {
    --teal: #00a8a4;
    --teal-deep: #008f8b;
    --charcoal: #333132;
    --ink: #2a2a2a;
    --white: #ffffff;
    --backdrop: #e9e7e4;
    --photo-light: #c9c5c2;
    --photo-dark: #6f6a67;
  }
  * { box-sizing: border-box; margin: 0; padding: 0; }
  html, body {
    width: 1200px; height: 1000px; overflow: hidden;
    background: var(--backdrop);
    font-family: "Open Sans", sans-serif;
  }
  .card {
    position: absolute; left: 220px;
    width: 760px; height: 434px;
    overflow: hidden;
    box-shadow: 0 10px 28px rgba(0,0,0,.18);
  }

  /* Front */
  .card-front { top: 44px; }
  .front-photo {
    position: absolute; inset: 0;
    background: linear-gradient(160deg, var(--photo-light) 0%, #a9a4a0 45%, var(--photo-dark) 100%);
  }
  .front-band {
    position: absolute; left: 0; right: 0; top: 112px; height: 232px;
    background: var(--teal);
    text-align: center; color: var(--white);
    padding-top: 30px;
  }
  .front-title {
    font-size: 46px; font-weight: 400; color: var(--ink);
    letter-spacing: 1px; line-height: 1.1; margin-bottom: 16px;
  }
  .front-line {
    font-size: 17px; font-weight: 400; letter-spacing: .5px; line-height: 1.55;
  }

  /* Back */
  .card-back { top: 522px; background: var(--teal); }
  .back-name-band {
    position: absolute; left: 0; right: 0; top: 60px; height: 110px;
    background: var(--charcoal);
    padding: 20px 90px 0 0; text-align: right;
  }
  .person-name {
    font-size: 42px; line-height: 1; color: var(--white); letter-spacing: .5px;
  }
  .person-name strong { font-weight: 700; }
  .person-name span { font-weight: 400; }
  .person-role {
    font-size: 21px; color: var(--teal); margin-top: 4px;
  }
  .band-icon { position: absolute; right: 34px; top: 34px; width: 40px; height: 34px; }

  .contact-list { position: absolute; right: 34px; top: 188px; width: 520px; }
  .contact-row {
    display: flex; justify-content: flex-end; align-items: center; gap: 14px;
    color: var(--white); font-size: 19px; line-height: 1.3;
  }
  .contact-row + .contact-row { margin-top: 14px; }
  .contact-row .lines { text-align: right; }
  .icon { width: 36px; height: 36px; flex: none; }
  .icon-dot { width: 36px; height: 36px; border-radius: 50%; background: var(--charcoal); flex: none; }

  .brand-mark {
    position: absolute; left: 70px; top: 262px;
    font-size: 40px; font-weight: 400; line-height: 1; color: var(--ink);
    letter-spacing: 1px;
  }
  .back-foot-band {
    position: absolute; left: 0; right: 0; bottom: 0; height: 58px;
    background: var(--charcoal);
  }
</style>
</head>
<body>

<section class="card card-front">
  <div class="front-photo" role="img" aria-label="Black and white photograph of a tattooed man seen from behind, hands clasped behind his head, overlooking a misty landscape"></div>
  <div class="front-band">
    <h1 class="front-title">PATHWAY BRIGHTLY</h1>
    <p class="front-line">MELBOURNE CBD &amp; GLOBALLY ON VOXLINK</p>
    <p class="front-line">TRANSPERSONAL / NONDUAL / EXISTENTIAL</p>
    <p class="front-line">FOLLOW YOUR BLISS</p>
  </div>
</section>

<section class="card card-back">
  <div class="back-name-band">
    <h2 class="person-name"><strong>MARCUS</strong> <span>HALBRENN</span></h2>
    <p class="person-role">Registered Career Counsellor</p>
    <svg class="band-icon" viewBox="0 0 40 34" aria-hidden="true">
      <path d="M3 9 Q20 -1 37 9 L33 14 L27 11 L27 7 Q20 4 13 7 L13 11 L7 14 Z" fill="var(--ink)"/>
      <rect x="9" y="15" width="22" height="16" rx="3" fill="var(--ink)"/>
      <circle cx="20" cy="23" r="4" fill="var(--charcoal)"/>
    </svg>
  </div>

  <div class="contact-list">
    <div class="contact-row">
      <div class="lines">+61(0) 412 968 204<br>www.pathwaybrightly.com</div>
      <svg class="icon" viewBox="0 0 36 36" aria-hidden="true">
        <circle cx="18" cy="18" r="16" fill="none" stroke="var(--charcoal)" stroke-width="3"/>
        <ellipse cx="18" cy="18" rx="7" ry="16" fill="none" stroke="var(--charcoal)" stroke-width="2.5"/>
        <line x1="2" y1="18" x2="34" y2="18" stroke="var(--charcoal)" stroke-width="2.5"/>
        <line x1="5" y1="10" x2="31" y2="10" stroke="var(--charcoal)" stroke-width="2"/>
        <line x1="5" y1="26" x2="31" y2="26" stroke="var(--charcoal)" stroke-width="2"/>
      </svg>
    </div>
    <div class="contact-row">
      <div class="lines">marcus@pathwaybrightly.com<br>www.pathwaybrightly.com</div>
      <span style="width:36px;flex:none"></span>
    </div>
    <div class="contact-row">
      <div class="lines">pathwaybrightly</div>
      <span class="icon-dot" aria-hidden="true"></span>
    </div>
  </div>

  <div class="brand-mark">PATHWAY<br>BRIGHTLY</div>
  <div class="back-foot-band"></div>
</section>

</body>
</html>
```